Product label required for my supplement company

Hi, I have attached the project description for my product label. Kindly feel free to submit your designs as I'll be awarding the project within 2 days. Hello! quick message that was left out of the original info:
-The bottles these labels will be on is white
-The "V" in Verdo Roots is a stock image and will need some modification for us to use as a shortened logo for this product and make it unique to our brand.

```html
<!DOCTYPE html>
<html lang="en">
<head>
<meta charset="utf-8">
<title>Verdo Roots – Chocolate Label</title>
<link rel="stylesheet" href="https://fonts.googleapis.com/css2?family=Montserrat:wght@400;600;800&family=Playfair+Display:wght@700&family=Dancing+Script:wght@700&display=swap">
<style>
  :root {
    --page: #ffffff;
    --lime: #e4ef2a;
    --green-light: #a9c93c;
    --green-mid: #8fb236;
    --green-deep: #6e9a2a;
    --ink: #1d1d1b;
    --ink-soft: #4d5a22;
    --brown: #7a2a12;
    --orange: #e06a12;
    --white: #ffffff;
    --choc: #4a2417;
    --seed-pea: #9ccc4a;
    --seed-hemp: #6f9a3a;
    --seed-almond: #d49a4a;
    --seed-pumpkin: #b9c24a;
    --seed-sunflower: #e8b321;
  }
  * { box-sizing: border-box; margin: 0; padding: 0; }
  html, body {
    width: 1200px; height: 675px; overflow: hidden;
    background: var(--page);
    font-family: "Montserrat", Arial, sans-serif;
  }
  .label {
    position: absolute; left: 40px; top: 128px;
    width: 1120px; height: 420px;
    background: linear-gradient(120deg, var(--green-light) 0%, var(--green-mid) 45%, var(--green-light) 70%, var(--green-deep) 100%);
    border-top: 14px solid var(--lime);
    border-bottom: 14px solid var(--lime);
    overflow: hidden;
  }
  .label__sweep { position: absolute; inset: 0; }

  .brand {
    position: absolute; left: 60px; top: 46px;
    display: flex; align-items: center; gap: 10px;
  }
  .brand__mark { width: 18px; height: 18px; background: var(--ink); }
  .brand__name {
    font-weight: 800; font-size: 40px; color: var(--ink);
    line-height: 1; white-space: nowrap;
  }

  .claims { position: absolute; left: 18px; top: 40px; display: flex; flex-direction: column; gap: 62px; }
  .claim { display: flex; flex-direction: column; align-items: center; width: 30px; }
  .claim svg { width: 24px; height: 24px; }
  .claim__text { font-size: 6px; color: var(--ink-soft); margin-top: 2px; text-align: center; }

  .protein { position: absolute; left: 112px; top: 140px; color: var(--ink-soft); text-align: center; }
  .protein__amount { font-size: 22px; font-weight: 600; }
  .protein__unit { font-size: 10px; }

  .chocolate-art {
    position: absolute; left: 70px; top: 230px; width: 190px; height: 150px;
    background: radial-gradient(ellipse at 50% 80%, var(--brown) 0%, var(--choc) 40%, rgba(74,36,23,0) 72%);
    opacity: .85;
  }

  .emblem {
    position: absolute; left: 390px; top: 38px; width: 250px; height: 190px;
    display: flex; align-items: center; justify-content: center; gap: 12px;
  }
  .emblem__dot { width: 34px; height: 34px; border-radius: 50%; background: var(--white); }
  .emblem__name { font-weight: 800; font-size: 30px; color: var(--white); line-height: 1.05; text-transform: uppercase; }

  .product { position: absolute; left: 300px; top: 232px; width: 430px; text-align: center; }
  .product__line {
    font-family: "Playfair Display", Georgia, serif; font-weight: 700;
    font-size: 38px; color: var(--brown); line-height: 1.05;
  }
  .product__flavour {
    font-family: "Dancing Script", cursive; font-weight: 700;
    font-size: 58px; color: var(--brown); margin-top: 4px;
  }

  .ingredients { position: absolute; left: 760px; top: 20px; display: flex; flex-direction: column; gap: 10px; list-style: none; }
  .ingredient { display: flex; align-items: center; gap: 16px; height: 64px; }
  .ingredient__name { width: 70px; font-size: 13px; font-style: italic; color: var(--ink); text-align: right; }
  .ingredient__art { width: 48px; height: 48px; border-radius: 50%; }
  .ingredient__art--pea { background: var(--seed-pea); }
  .ingredient__art--hemp { background: var(--seed-hemp); }
  .ingredient__art--almond { background: var(--seed-almond); }
  .ingredient__art--pumpkin { background: var(--seed-pumpkin); }
  .ingredient__art--sunflower { background: var(--seed-sunflower); }

  .notes { position: absolute; left: 930px; top: 28px; width: 170px; display: flex; flex-direction: column; gap: 26px; }
  .note__title { font-size: 14px; font-weight: 600; color: var(--orange); margin-bottom: 4px; }
  .note__body { font-size: 10px; color: var(--white); line-height: 1.4; }
  .storage { position: absolute; left: 930px; bottom: 18px; font-size: 8px; color: var(--ink-soft); }
</style>
</head>
<body>
  <section class="label">
    <svg class="label__sweep" viewBox="0 0 1120 392" preserveAspectRatio="none" aria-hidden="true">
      <path d="M0 392 C 300 300, 600 360, 1120 150 L1120 392 Z" fill="#7ea630" opacity=".35"/>
      <path d="M0 0 C 320 80, 700 20, 1120 110 L1120 0 Z" fill="#c4dc4a" opacity=".3"/>
    </svg>

    <div class="claims">
      <div class="claim">
        <svg viewBox="0 0 24 24"><circle cx="12" cy="12" r="10" fill="none" stroke="#4d5a22" stroke-width="1.5"/><path d="M7 12l3.5 3.5L17 9" fill="none" stroke="#4d5a22" stroke-width="1.8"/></svg>
        <span class="claim__text">Vegan</span>
      </div>
      <div class="claim">
        <svg viewBox="0 0 24 24"><circle cx="12" cy="12" r="10" fill="none" stroke="#4d5a22" stroke-width="1.5"/><path d="M7 12l3.5 3.5L17 9" fill="none" stroke="#4d5a22" stroke-width="1.8"/></svg>
        <span class="claim__text">Gluten Free</span>
      </div>
      <div class="claim">
        <svg viewBox="0 0 24 24"><circle cx="12" cy="12" r="10" fill="none" stroke="#4d5a22" stroke-width="1.5"/><path d="M7 12l3.5 3.5L17 9" fill="none" stroke="#4d5a22" stroke-width="1.8"/></svg>
        <span class="claim__text">Non GMO</span>
      </div>
      <div class="claim">
        <svg viewBox="0 0 24 24"><circle cx="12" cy="12" r="10" fill="none" stroke="#4d5a22" stroke-width="1.5"/><path d="M7 12l3.5 3.5L17 9" fill="none" stroke="#4d5a22" stroke-width="1.8"/></svg>
        <span class="claim__text">Dairy Free</span>
      </div>
    </div>

    <div class="brand">
      <span class="brand__mark"></span>
      <span class="brand__name">Fuel Blends</span>
    </div>

    <div class="protein">
      <div class="protein__amount">22g</div>
      <div class="protein__unit">Protein</div>
    </div>

    <div class="chocolate-art" role="img" aria-label="Chocolate pieces splashing into melted chocolate"></div>

    <div class="emblem">
      <span class="emblem__dot"></span>
      <span class="emblem__name">Verdo<br>Roots</span>
    </div>

    <div class="product">
      <div class="product__line">Food &amp; Drink</div>
      <div class="product__line">Fuel Blends</div>
      <div class="product__flavour">Chocolate</div>
    </div>

    <ul class="ingredients">
      <li class="ingredient"><span class="ingredient__name">Pea</span><span class="ingredient__art ingredient__art--pea" role="img" aria-label="Green pea pod"></span></li>
      <li class="ingredient"><span class="ingredient__name">Hemp</span><span class="ingredient__art ingredient__art--hemp" role="img" aria-label="Hemp leaf"></span></li>
      <li class="ingredient"><span class="ingredient__name">Almond</span><span class="ingredient__art ingredient__art--almond" role="img" aria-label="Almonds"></span></li>
      <li class="ingredient"><span class="ingredient__name">Pumpkin</span><span class="ingredient__art ingredient__art--pumpkin" role="img" aria-label="Pumpkin seeds"></span></li>
      <li class="ingredient"><span class="ingredient__name">Sunflower</span><span class="ingredient__art ingredient__art--sunflower" role="img" aria-label="Sunflower head"></span></li>
    </ul>

    <div class="notes">
      <div class="note">
        <div class="note__title">Plant Protein</div>
        <p class="note__body">Five seeds blended for smooth daily fuel.</p>
      </div>
      <div class="note">
        <div class="note__title">Rich Flavour</div>
        <p class="note__body">Real cocoa taste with no added sugar.</p>
      </div>
      <div class="note">
        <div class="note__title">Serving</div>
        <p class="note__body">Mix one scoop with water or plant milk.</p>
      </div>
    </div>

    <p class="storage">Store in a cool dry place.</p>
  </section>
</body>
</html>
```